Business Card Design Project

you do have a logo of ares but open for anything new . main color is royal blue and white ...are give us some ideas if you like
company name is Merrow's Lawn, Tree and Landscape Contractor
PAVERS
-Pool Decks
-Driveways
-Patios
-Sidewalks & Steps
-Fire Pits
-Retaining Walls
-Layover
-All Patterns and Colors
-To view and/or create your color choice and Patterns visit www.fambleknotstone.com
Custom Concrete Work
-Sea Walls
-Slabs
-Sidewalks
-Concrete Stamping
-Custom Walls
-Custom Curbing
-Concrete Stain (Acid and Eco-Stains available)
-Concrete Sealer
-All Concrete Jobs Call And Ask
-To view and/or create your color choice visit Hollin Tint's Stoneboard Swatch app at www.stoneboardswatch.com
Pest Control
-Lawns insect, fungus and weed control
-Lawn Fertilization
-Outdoor Pest
- Indoor Pest Control
-Termite Control
-White Fly Treatment
-Rodent Control
IRRIGATION
-installs
-Repair
-Service of Irrigation
Landscape & Installation (residential and commercial)
-Full Lawn Care Service
-Landscape Maintenance
-Weed Control in Flower Beds
-Sod Installation
-Tree Trimming
-Tree Removal
-Bush Pruning
-All Tree & Plant Treatment for Bug, Dieses & Fungus Control
Landscape Material Delivery & Install
-Plants and Tree Install
-Rock, Mulch, Soil, Sand and Riprap
-Weed mat
-Boulders and Flagstone
-Pavers
Call 941.555.0172 for more information.
Residential, Commercial, condos, H.O.A
Lic. & Ins.

```html
<!DOCTYPE html>
<html lang="en">
<head>
<meta charset="utf-8">
<title>Merrow's Lawn, Tree and Landscape Contractor — Business Card</title>
<link rel="stylesheet" href="https://fonts.googleapis.com/css2?family=Questrial&display=swap">
<style>
  :root {
    --stage: #2b2b2b;
    --card-light: #f4f4f3;
    --card-shade: #dcdcda;
    --olive: #6a6426;
    --ink: #151515;
    --dusk-top: #9a8fa6;
    --dusk-mid: #4f5a4a;
    --dusk-low: #1f2a1c;
    --garden-top: #cfe0d8;
    --garden-mid: #6f9a4c;
    --garden-low: #3d5e2c;
    --house-top: #c8d2dc;
    --house-mid: #c9a99a;
    --house-low: #5f8a3c;
  }
  * { box-sizing: border-box; margin: 0; padding: 0; }
  html, body {
    width: 1200px; height: 900px; overflow: hidden;
    background: var(--stage);
    font-family: "Questrial", "Century Gothic", sans-serif;
  }
  .canvas {
    position: relative; width: 1200px; height: 900px;
  }
  .card {
    position: absolute; left: 320px; width: 560px; height: 320px;
    background: linear-gradient(160deg, var(--card-light) 0%, var(--card-shade) 100%);
    overflow: hidden;
    box-shadow: 0 10px 30px rgba(0,0,0,0.5);
  }
  .card--front { top: 100px; }
  .card--back { top: 480px; }

  /* Front */
  .front-photo {
    position: absolute; left: 0; top: 0; width: 100%; height: 62%;
    background: linear-gradient(180deg, var(--dusk-top) 0%, var(--dusk-mid) 55%, var(--dusk-low) 100%);
  }
  .front-band {
    position: absolute; left: 0; bottom: 0; width: 100%; height: 38%;
    display: flex; align-items: center; justify-content: flex-end;
    padding-right: 40px;
  }

  /* Brand name block */
  .brand {
    display: flex; align-items: center; gap: 10px;
    color: var(--olive);
  }
  .brand-dot {
    width: 26px; height: 26px; border-radius: 50%;
    background: var(--olive); flex: none;
  }
  .brand-text { line-height: 1.05; }
  .brand-name { font-size: 30px; letter-spacing: 1px; display: block; }
  .brand-line { font-size: 9px; letter-spacing: 0.5px; display: block; }

  /* Back */
  .back-strip {
    position: absolute; left: 0; top: 0; width: 37%; height: 100%;
    display: flex; flex-direction: column;
    border-right: 1px solid #bdbdbb;
  }
  .photo-garden {
    height: 37%;
    background: linear-gradient(180deg, var(--garden-top) 0%, var(--garden-mid) 40%, var(--garden-low) 100%);
  }
  .back-brand {
    height: 28%; display: flex; align-items: center; padding-left: 14px;
    background: var(--card-light);
  }
  .back-brand .brand-name { font-size: 24px; }
  .back-brand .brand-line { font-size: 7.5px; }
  .back-brand .brand-dot { width: 20px; height: 20px; }
  .photo-house {
    flex: 1;
    background: linear-gradient(180deg, var(--house-top) 0%, var(--house-mid) 55%, var(--house-low) 100%);
  }
  .contact {
    position: absolute; left: 37%; top: 0; width: 63%; height: 100%;
    display: flex; flex-direction: column; align-items: center; justify-content: center;
    text-align: center; gap: 2px;
  }
  .contact-label { color: var(--olive); font-size: 15px; letter-spacing: 0.5px; margin-top: 6px; }
  .contact-value { color: var(--ink); font-size: 16px; }
</style>
</head>
<body>
<main class="canvas">
  <section class="card card--front">
    <div class="front-photo" role="img" aria-label="Dusk photograph of a lit house with palm trees and a pool"></div>
    <div class="front-band">
      <div class="brand">
        <span class="brand-dot"></span>
        <span class="brand-text">
          <span class="brand-name">Merrow's</span>
          <span class="brand-line">Lawn, Tree and Landscape Contractor</span>
        </span>
      </div>
    </div>
  </section>

  <section class="card card--back">
    <div class="back-strip">
      <div class="photo-garden" role="img" aria-label="Photograph of a curved paver walkway beside a lawn and flower beds"></div>
      <div class="back-brand">
        <div class="brand">
          <span class="brand-dot"></span>
          <span class="brand-text">
            <span class="brand-name">Merrow's</span>
            <span class="brand-line">Lawn, Tree and Landscape Contractor</span>
          </span>
        </div>
      </div>
      <div class="photo-house" role="img" aria-label="Photograph of a stucco house with a landscaped front lawn"></div>
    </div>
    <div class="contact">
      <p class="contact-label">PHONE NUMBER</p>
      <p class="contact-value">000 000 000</p>
      <p class="contact-label">ADDRESS</p>
      <p class="contact-value">Your address</p>
      <p class="contact-label">EMAIL</p>
      <p class="contact-value">yourname@domain.com</p>
    </div>
  </section>
</main>
</body>
</html>
```